A building General Contractor is looking for a business card design

I need a business card designed. The company "Stoneridge Framing Contractors" is a general contractor for commercial buildings and pre-engineered metal buildings.

```html
<!DOCTYPE html>
<html lang="en">
<head>
<meta charset="utf-8">
<title>Stoneridge Framing Contractors – Business Cards</title>
<link rel="stylesheet" href="https://fonts.googleapis.com/css2?family=Barlow:wght@400;600;800&display=swap">
<style>
  :root {
    --page-bg: #ebe9e9;
    --light-photo-a: #f1f4f6;
    --light-photo-b: #cdd6dd;
    --dark-photo-a: #2d2927;
    --dark-photo-b: #141212;
    --ink-dark: #3a3a3c;
    --ink-soft: #5c5f63;
    --ink-light: #e6e6e6;
    --ink-light-soft: #b9b9b9;
    --icon-dark: #4a4b4e;
    --icon-light: #8a8a8a;
  }
  * { margin: 0; padding: 0; box-sizing: border-box; }
  html, body { width: 1200px; height: 2918px; overflow: hidden; }
  body {
    background: var(--page-bg);
    font-family: "Barlow", sans-serif;
  }
  .card-row {
    height: 972.67px;
    display: flex;
    align-items: center;
    justify-content: center;
    gap: 60px;
  }
  .card {
    position: relative;
    width: 520px;
    height: 297px;
    overflow: hidden;
    box-shadow: 0 2px 6px rgba(0,0,0,0.12);
  }
  .card-photo {
    position: absolute;
    inset: 0;
  }
  .card--light .card-photo {
    background: linear-gradient(135deg, var(--light-photo-a) 0%, var(--light-photo-b) 100%);
  }
  .card--dark .card-photo {
    background: linear-gradient(135deg, var(--dark-photo-a) 0%, var(--dark-photo-b) 100%);
  }
  .card-content { position: absolute; inset: 0; }

  .brand-name {
    font-weight: 800;
    text-transform: uppercase;
    line-height: 1;
    letter-spacing: 0.5px;
    display: flex;
    align-items: center;
    gap: 10px;
  }
  .brand-mark {
    width: 14px;
    height: 14px;
    flex: none;
  }
  .card--light .brand-name { color: var(--ink-dark); }
  .card--light .brand-mark { background: var(--ink-dark); }
  .card--dark .brand-name { color: var(--ink-light); }
  .card--dark .brand-mark { background: var(--ink-light); }

  /* front */
  .front .brand-name {
    position: absolute;
    left: 34px;
    top: 40px;
    font-size: 21px;
    width: 200px;
  }
  .divider {
    position: absolute;
    left: 238px;
    top: 40px;
    width: 1px;
    height: 200px;
  }
  .card--light .divider { background: var(--ink-soft); }
  .card--dark .divider { background: var(--ink-light-soft); }
  .divider::after {
    content: "";
    position: absolute;
    left: -4px;
    top: 0;
    border-left: 4.5px solid transparent;
    border-right: 4.5px solid transparent;
    border-top: 10px solid currentColor;
  }
  .card--light .divider { color: var(--ink-dark); }
  .card--dark .divider { color: var(--ink-light-soft); }

  .contact-block {
    position: absolute;
    left: 262px;
    top: 112px;
  }
  .contact-title {
    font-weight: 600;
    font-size: 14px;
    text-transform: uppercase;
    letter-spacing: 0.6px;
  }
  .contact-sub {
    font-size: 10px;
    text-transform: uppercase;
    letter-spacing: 1px;
    margin-top: 2px;
    margin-bottom: 14px;
  }
  .contact-list { list-style: none; }
  .contact-item {
    display: flex;
    align-items: center;
    gap: 9px;
    font-size: 12.5px;
    margin-top: 6px;
  }
  .contact-icon {
    width: 15px;
    height: 15px;
    display: flex;
    align-items: center;
    justify-content: center;
    flex: none;
  }
  .contact-icon svg { width: 10px; height: 10px; }
  .card--light .contact-title, .card--light .contact-item { color: var(--ink-dark); }
  .card--light .contact-sub { color: var(--ink-soft); }
  .card--light .contact-icon { background: var(--icon-dark); }
  .card--dark .contact-title, .card--dark .contact-item { color: var(--ink-light); }
  .card--dark .contact-sub { color: var(--ink-light-soft); }
  .card--dark .contact-icon { background: var(--icon-light); }

  /* back */
  .back .card-content {
    display: flex;
    align-items: center;
    justify-content: center;
  }
  .back .brand-name {
    font-size: 26px;
    width: 260px;
  }
</style>
</head>
<body>

<section class="card-row">
  <article class="card card--light front">
    <div class="card-photo" role="img" aria-label="Pale photograph of a glass office tower seen from below"></div>
    <div class="card-content">
      <div class="brand-name"><span class="brand-mark"></span>Stoneridge Framing Contractors</div>
      <div class="divider"></div>
      <div class="contact-block">
        <p class="contact-title">Stoneridge Framing</p>
        <p class="contact-sub">Contractors</p>
        <ul class="contact-list">
          <li class="contact-item"><span class="contact-icon"><svg viewBox="0 0 10 10"><path d="M2 1l2 2-1 1c.6 1.3 1.7 2.4 3 3l1-1 2 2-1.5 1.5C4.5 9 1 5.5.5 2.5z" fill="#fff"/></svg></span>+00 4821 5XXX 7730</li>
          <li class="contact-item"><span class="contact-icon"><svg viewBox="0 0 10 10"><rect x="1" y="2.5" width="8" height="5" fill="none" stroke="#fff"/><path d="M1 2.5l4 3 4-3" fill="none" stroke="#fff"/></svg></span>stoneridgeframing@mail.com</li>
          <li class="contact-item"><span class="contact-icon"><svg viewBox="0 0 10 10"><circle cx="5" cy="5" r="3.8" fill="none" stroke="#fff"/><path d="M1.2 5h7.6M5 1.2c-2 2.4-2 5.2 0 7.6M5 1.2c2 2.4 2 5.2 0 7.6" fill="none" stroke="#fff" stroke-width=".8"/></svg></span>www.stoneridgeframing.com</li>
        </ul>
      </div>
    </div>
  </article>
  <article class="card card--light back">
    <div class="card-photo" role="img" aria-label="Pale photograph of a glass office tower seen from below"></div>
    <div class="card-content">
      <div class="brand-name"><span class="brand-mark"></span>Stoneridge Framing Contractors</div>
    </div>
  </article>
</section>

<section class="card-row">
  <article class="card card--light front">
    <div class="card-photo" role="img" aria-label="Pale photograph of a glass office tower seen from below"></div>
    <div class="card-content">
      <div class="brand-name"><span class="brand-mark"></span>Stoneridge Framing Contractors</div>
      <div class="divider"></div>
      <div class="contact-block">
        <p class="contact-title">Stoneridge Framing</p>
        <p class="contact-sub">Contractors</p>
        <ul class="contact-list">
          <li class="contact-item"><span class="contact-icon"><svg viewBox="0 0 10 10"><path d="M2 1l2 2-1 1c.6 1.3 1.7 2.4 3 3l1-1 2 2-1.5 1.5C4.5 9 1 5.5.5 2.5z" fill="#fff"/></svg></span>+00 4821 5XXX 7730</li>
          <li class="contact-item"><span class="contact-icon"><svg viewBox="0 0 10 10"><rect x="1" y="2.5" width="8" height="5" fill="none" stroke="#fff"/><path d="M1 2.5l4 3 4-3" fill="none" stroke="#fff"/></svg></span>stoneridgeframing@mail.com</li>
          <li class="contact-item"><span class="contact-icon"><svg viewBox="0 0 10 10"><circle cx="5" cy="5" r="3.8" fill="none" stroke="#fff"/><path d="M1.2 5h7.6M5 1.2c-2 2.4-2 5.2 0 7.6M5 1.2c2 2.4 2 5.2 0 7.6" fill="none" stroke="#fff" stroke-width=".8"/></svg></span>www.stoneridgeframing.com</li>
        </ul>
      </div>
    </div>
  </article>
  <article class="card card--dark back">
    <div class="card-photo" role="img" aria-label="Dark photograph of a glass office tower seen from below"></div>
    <div class="card-content">
      <div class="brand-name"><span class="brand-mark"></span>Stoneridge Framing Contractors</div>
    </div>
  </article>
</section>

<section class="card-row">
  <article class="card card--dark front">
    <div class="card-photo" role="img" aria-label="Dark photograph of a glass office tower seen from below"></div>
    <div class="card-content">
      <div class="brand-name"><span class="brand-mark"></span>Stoneridge Framing Contractors</div>
      <div class="divider"></div>
      <div class="contact-block">
        <p class="contact-title">Stoneridge Framing</p>
        <p class="contact-sub">Contractors</p>
        <ul class="contact-list">
          <li class="contact-item"><span class="contact-icon"><svg viewBox="0 0 10 10"><path d="M2 1l2 2-1 1c.6 1.3 1.7 2.4 3 3l1-1 2 2-1.5 1.5C4.5 9 1 5.5.5 2.5z" fill="#222"/></svg></span>+00 4821 5XXX 7730</li>
          <li class="contact-item"><span class="contact-icon"><svg viewBox="0 0 10 10"><rect x="1" y="2.5" width="8" height="5" fill="none" stroke="#222"/><path d="M1 2.5l4 3 4-3" fill="none" stroke="#222"/></svg></span>stoneridgeframing@mail.com</li>
          <li class="contact-item"><span class="contact-icon"><svg viewBox="0 0 10 10"><circle cx="5" cy="5" r="3.8" fill="none" stroke="#222"/><path d="M1.2 5h7.6M5 1.2c-2 2.4-2 5.2 0 7.6M5 1.2c2 2.4 2 5.2 0 7.6" fill="none" stroke="#222" stroke-width=".8"/></svg></span>www.stoneridgeframing.com</li>
        </ul>
      </div>
    </div>
  </article>
  <article class="card card--dark back">
    <div class="card-photo" role="img" aria-label="Dark photograph of a glass office tower seen from below"></div>
    <div class="card-content">
      <div class="brand-name"><span class="brand-mark"></span>Stoneridge Framing Contractors</div>
    </div>
  </article>
</section>

</body>
</html>
```